Business Card Design for company

We want new business cards. We'd like something different-- yet still highly professional. Our tagline is Providing leadership, delivering success. Stock photos are ok, as long as they are relevant and look upscale.

Target Market(s)

Architecture/Business Management Consulting/Engineering Consulting

Contact Information for Business Card

dark gray background with pops of blue might be good, but you tell me. You're the designers. Rounded corners might be nice, but again, you tell me.

Font styles to use
Serif
Sans Serif

Colors
3276b5
5c5c5c
9d9d9d
fbfbfb

Requirements
Nice to have
• Something different, but still very professional.

```html
<!DOCTYPE html>
<html lang="en">
<head>
<meta charset="utf-8">
<title>VTR Consulting – Business Card Set</title>
<link href="https://fonts.googleapis.com/css2?family=Josefin+Sans:wght@400;600;700&family=Montserrat:wght@400;600&display=swap" rel="stylesheet">
<style>
  :root{
    --stage:#333333;
    --brand-blue:#3276b5;
    --deep-blue:#2a5d8f;
    --mid-gray:#5c5c5c;
    --card-gray:#9d9d9d;
    --paper:#ffffff;
    --ink:#111111;
    --light:#fbfbfb;
  }
  *{margin:0;padding:0;box-sizing:border-box}
  html,body{width:1200px;height:894px;overflow:hidden;background:var(--stage)}
  .stage{position:relative;width:1200px;height:894px;background:var(--stage)}
  .card{position:absolute;width:468px;height:289px;border-radius:27px;overflow:hidden;background:var(--paper);font-family:"Josefin Sans",sans-serif}
  .card--gray{background:var(--card-gray)}
  .card--front-white{left:94px;top:143px}
  .card--front-gray{left:651px;top:143px}
  .card--back-white{left:94px;top:478px}
  .card--back-gray{left:651px;top:478px}
  .card-art{position:absolute;inset:0;width:468px;height:289px}

  .holder-name{position:absolute;left:25px;top:50px;font-size:29px;font-weight:700;letter-spacing:.5px;color:var(--ink);line-height:1}
  .holder-role{position:absolute;left:25px;top:86px;font-size:11px;color:var(--brand-blue);letter-spacing:.3px}
  .card--gray .holder-name{color:var(--light)}
  .card--gray .holder-role{color:var(--ink)}

  .contact{position:absolute;left:0;display:flex;align-items:center;font-size:9px;color:var(--ink)}
  .card--gray .contact{color:var(--light)}
  .contact svg{position:absolute;left:-11px;top:-11px}
  .contact span{position:absolute;left:29px;white-space:nowrap;line-height:1.3}
  .contact--phone{top:138px}
  .contact--web{top:172px}
  .contact--address{top:202px}
  .contact--address span{font-size:7px;top:-5px}

  .site{position:absolute;left:0;width:468px;text-align:center;font-size:11px;color:var(--ink);top:270px}
  .card--front-white .site,.card--front-gray .site{width:290px}
  .card--gray .site{color:var(--light)}

  .wordmark{position:absolute;text-align:center;font-family:"Montserrat",sans-serif;font-weight:600;color:var(--deep-blue);line-height:1}
  .wordmark .wm-main{display:block}
  .wordmark .wm-sub{display:block;letter-spacing:1px}
  .card--front-white .wordmark,.card--front-gray .wordmark{left:234px;width:200px;top:112px}
  .card--front-white .wm-main,.card--front-gray .wm-main{font-size:52px}
  .card--front-white .wm-sub,.card--front-gray .wm-sub{font-size:12.5px;margin-top:4px}
  .card--back-white .wordmark,.card--back-gray .wordmark{left:84px;width:300px;top:64px}
  .card--back-white .wm-main,.card--back-gray .wm-main{font-size:70px}
  .card--back-white .wm-sub,.card--back-gray .wm-sub{font-size:17px;margin-top:6px}
</style>
</head>
<body>
<div class="stage">

  <svg width="0" height="0" style="position:absolute" aria-hidden="true">
    <defs>
      <linearGradient id="skyline-tone" x1="0" y1="0" x2="1" y2="1">
        <stop offset="0" stop-color="#1f4f86"/>
        <stop offset=".45" stop-color="#9fc0e0"/>
        <stop offset=".7" stop-color="#d9e6f3"/>
        <stop offset="1" stop-color="#24578e"/>
      </linearGradient>
      <clipPath id="front-photo-clip"><polygon points="305,0 468,0 468,289 330,289 156,143"/></clipPath>
      <clipPath id="back-photo-clip"><polygon points="0,0 468,0 468,78 234,250 0,103"/></clipPath>
      <g id="front-art">
        <polygon points="272,0 468,0 468,289 294,289 143,143" fill="var(--brand-blue)"/>
        <g clip-path="url(#front-photo-clip)">
          <rect width="468" height="289" fill="url(#skyline-tone)"/>
          <rect x="150" y="63" width="318" height="161" fill="#ffffff" opacity=".78"/>
        </g>
      </g>
      <g id="back-art">
        <g clip-path="url(#back-photo-clip)">
          <rect width="468" height="289" fill="url(#skyline-tone)"/>
          <polygon points="112,0 354,0 354,160 234,250 112,160" fill="#ffffff" opacity=".78"/>
        </g>
      </g>
      <g id="icon-phone">
        <circle cx="11" cy="11" r="11" fill="var(--brand-blue)"/>
        <path d="M14 8.5c-.6 0-1 .5-1.3 1l-.5-.3c-.3.4-.3.9 0 1.4l2 2.2c.5.4 1 .5 1.4.2l-.3-.5c.6-.3 1-.8 1-1.4l-1.4-1.2z" fill="#fff" transform="translate(-2 -1)"/>
      </g>
      <g id="icon-mail">
        <circle cx="11" cy="11" r="11" fill="var(--brand-blue)"/>
        <rect x="12" y="7.5" width="8" height="6" fill="none" stroke="#fff" stroke-width="1"/>
        <path d="M12 7.5l4 3.2 4-3.2" fill="none" stroke="#fff" stroke-width="1"/>
      </g>
      <g id="icon-pin">
        <circle cx="11" cy="11" r="11" fill="var(--brand-blue)"/>
        <path d="M16 6.5a3 3 0 0 0-3 3c0 2.2 3 5 3 5s3-2.8 3-5a3 3 0 0 0-3-3z" fill="#fff"/>
        <circle cx="16" cy="9.5" r="1.1" fill="var(--brand-blue)"/>
      </g>
    </defs>
  </svg>

  <!-- Front, white -->
  <section class="card card--front-white">
    <svg class="card-art" viewBox="0 0 468 289" role="img" aria-label="Upward view of glass office towers in blue tones"><use href="#front-art"/></svg>
    <h1 class="holder-name">RASHID</h1>
    <p class="holder-role">GRAND MANAGER</p>
    <div class="contact contact--phone"><svg width="22" height="22"><use href="#icon-phone"/></svg><span>123 - 456 - 789</span></div>
    <div class="contact contact--web"><svg width="22" height="22"><use href="#icon-mail"/></svg><span>YOURWEBSITE.COM</span></div>
    <div class="contact contact--address"><svg width="22" height="22"><use href="#icon-pin"/></svg><span>LAKEVIEW ROAD, BLOCK 4<br>HARBOUR 20418</span></div>
    <div class="wordmark"><span class="wm-main">VTR</span><span class="wm-sub">CONSULTING</span></div>
    <p class="site">YOURWEBSITE.COM</p>
  </section>

  <!-- Front, gray -->
  <section class="card card--gray card--front-gray">
    <svg class="card-art" viewBox="0 0 468 289" role="img" aria-label="Upward view of glass office towers in blue tones"><use href="#front-art"/></svg>
    <h1 class="holder-name">RASHID</h1>
    <p class="holder-role">GRAND MANAGER</p>
    <div class="contact contact--phone"><svg width="22" height="22"><use href="#icon-phone"/></svg><span>123 - 456 - 789</span></div>
    <div class="contact contact--web"><svg width="22" height="22"><use href="#icon-mail"/></svg><span>YOURWEBSITE.COM</span></div>
    <div class="contact contact--address"><svg width="22" height="22"><use href="#icon-pin"/></svg><span>LAKEVIEW ROAD, BLOCK 4<br>HARBOUR 20418</span></div>
    <div class="wordmark"><span class="wm-main">VTR</span><span class="wm-sub">CONSULTING</span></div>
    <p class="site">YOURWEBSITE.COM</p>
  </section>

  <!-- Back, white -->
  <section class="card card--back-white">
    <svg class="card-art" viewBox="0 0 468 289" role="img" aria-label="Upward view of glass office towers in blue tones"><use href="#back-art"/></svg>
    <div class="wordmark"><span class="wm-main">VTR</span><span class="wm-sub">CONSULTING</span></div>
    <p class="site">YOURWEBSITE.COM</p>
  </section>

  <!-- Back, gray -->
  <section class="card card--gray card--back-gray">
    <svg class="card-art" viewBox="0 0 468 289" role="img" aria-label="Upward view of glass office towers in blue tones"><use href="#back-art"/></svg>
    <div class="wordmark"><span class="wm-main">VTR</span><span class="wm-sub">CONSULTING</span></div>
    <p class="site">YOURWEBSITE.COM</p>
  </section>

</div>
</body>
</html>
```